Harbor Renewal Large Loss Booklet

It will be a booklet brochure, 5 pages of front and back material and covers on both sides. Use the presentation files you already created to make it happen.
Updates

I realized the presentation files by which we were asking everyone to use were not updated. They are now posted with a little more detail. Thank you!

Target Market(s)

Facility Managers and VPs in Commercial Real Estate and Construction

Industry/Entity Type

Real Estate

Requirements
Must have
• Commercial real estate oriented, relational wording, large catastrophic loss events
Should not have
• Sales and closing type words, no residential themes

```html
<!DOCTYPE html>
<html lang="en">
<head>
<meta charset="utf-8">
<title>Harbor Renewal Large Loss Booklet – Spread</title>
<link href="https://fonts.googleapis.com/css2?family=Open+Sans:wght@400;600;700&display=swap" rel="stylesheet">
<style>
  :root {
    --bg: #ece7df;
    --paper: #ffffff;
    --amber: #e8a232;
    --amber-bar: #e39b22;
    --ink-blue: #1f5fa8;
    --white: #ffffff;
    --photo-dark-1: #2a2622;
    --photo-dark-2: #6b5a48;
    --photo-sky-1: #2f7fd0;
    --photo-sky-2: #9cc7ee;
    --scaffold: #5d6b6f;
  }
  * { box-sizing: border-box; margin: 0; padding: 0; }
  html, body { width: 1200px; height: 800px; overflow: hidden; }
  body {
    background: var(--bg);
    font-family: "Open Sans", Arial, sans-serif;
    position: relative;
  }
  .spread {
    position: absolute;
    left: 30px; top: 190px;
    width: 1140px; height: 420px;
    display: flex;
    box-shadow: 0 6px 18px rgba(0,0,0,.18);
  }
  .page { position: relative; width: 570px; height: 420px; overflow: hidden; background: var(--paper); }

  .page-left .photo-site {
    position: absolute; inset: 0;
    background: linear-gradient(160deg, var(--photo-dark-2) 0%, #4a3d32 40%, var(--photo-dark-1) 80%, #111 100%);
  }
  .intro-panel {
    position: absolute; left: 0; top: 0;
    width: 285px; height: 239px;
    background: var(--amber);
    color: var(--white);
    padding: 22px 24px 0 24px;
  }
  .intro-panel h2 { font-size: 10px; font-weight: 600; letter-spacing: .2px; margin-bottom: 11px; }
  .intro-panel p { font-size: 6.6px; line-height: 1.6; text-align: justify; margin-bottom: 9px; }

  .page-right { display: flex; }
  .service-column { width: 285px; height: 100%; background: var(--paper); padding-top: 26px; }
  .service-heading {
    width: 262px; height: 22px;
    background: var(--amber-bar);
    color: var(--white);
    font-size: 10px; font-weight: 600;
    display: flex; align-items: center;
    padding-left: 24px;
    margin-bottom: 14px;
  }
  .service-body { padding: 0 23px 0 24px; color: var(--ink-blue); }
  .service-body p { font-size: 6.6px; line-height: 1.55; text-align: justify; margin-bottom: 10px; }
  .photo-scaffold {
    width: 285px; height: 100%;
    background: linear-gradient(180deg, var(--photo-sky-1) 0%, var(--photo-sky-2) 35%, var(--scaffold) 75%, #3e4a4e 100%);
  }
</style>
</head>
<body>
  <div class="spread">
    <section class="page page-left">
      <div class="photo-site" role="img" aria-label="Crew clearing debris inside a damaged commercial building"></div>
      <div class="intro-panel">
        <h2>WHO WE ARE</h2>
        <p>Harbor Renewal Services partners with facility teams to restore commercial properties back to their pre-loss condition after emergency or catastrophic events primarily caused by water/flood damage, fire, bio-hazard/trauma events, and instances of mild to extensive mold growth. When called upon, we consider it both a privilege and responsibility to respond immediately, and our team of highly-trained technicians works alongside your managers to restore offices, warehouses, retail centers and construction sites affected by flood, fire, bio-hazard/trauma, or mold to their original condition while protecting operations, tenants and schedules.</p>
        <p>Harbor Renewal is prepared to support any sized loss in any type of commercial facility. We value long-term relationships with property owners and managers, and we are fully staffed and trained to handle large catastrophic losses across multiple sites. We work with all insurance carriers, and we coordinate closely with the adjusters who represent them.</p>
      </div>
    </section>
    <section class="page page-right">
      <div class="service-column">
        <h2 class="service-heading">WATER AND FLOOD RESTORATION</h2>
        <div class="service-body">
          <p>Harbor Renewal Services' mission is to get your facility dry and sanitary, help prevent mold growth, and keep your operations on the road to recovery.</p>
          <p>Water damage regardless of the source is something that will not improve on its own. From the moment a loss occurs, framing begins to swell, drywall begins to absorb moisture, equipment and inventory are adversely affected, and flooring systems begin to fail. Water MUST be removed to allow the structure to dry thoroughly.</p>
          <p>Water intrusion can disrupt not only your building, but also your tenants and business continuity. Whether a property has been damaged by flood waters, or the structure has suffered a loss due to burst mains, roof leaks, sprinkler discharge or failed plumbing systems, time is of the essence. Water intrusions cause damage to walls, floors, fixtures, inventory, and the structural integrity of property. The formation of molds, mildew, fungi, and other potentially hazardous growth can occur if not properly addressed. The longer the delay, the greater the amount of damage, and the longer it will take to return the site to a pre-loss condition. At Harbor Renewal Services, our goal is to restore your structure as quickly and efficiently as possible, to return your facility to its pre-loss state.</p>
          <p>Harbor Renewal Services 24 Hour Emergency Teams mobilize rapidly to begin the water mitigation and restoration process. Utilizing state of the art drying equipment, moisture meters, moisture mapping, and other industry technology, our licensed and insured technicians will communicate with your team every step of the way.</p>
        </div>
      </div>
      <div class="photo-scaffold" role="img" aria-label="Commercial building facade wrapped in scaffolding with a blue debris chute against a blue sky"></div>
    </section>
  </div>
</body>
</html>
```